Merrivale construction website for a high end luxury custom home builder

I need a website designed for a high end luxury custom home builder. I would like the website to host a number activities. A blog/vlog on the page where I can post about the projects being built how to's what to look out for during the build, A designated testimonial page but also having testimonials posted on the other pages like the gallery linked to the photos of the completed projects. a gallery page, an about us page, services page that demonstrate what we do and what we are capable of, and hopefully when I start winning awards, and awards page.
Home page
about us page
services page
gallery
testimonial
awards page but I my need to add that later.
I already have the domain name for the website. www.merrivaleconstruction.com.au
I recently completed a sketch hive page for my logo and will post the logo documents below.

Target Market(s)

I'd like to target professions with cash enough to build a house. I would like peolpe to understand that they are buy a price when they are getting quote to build there house. It seems like people just look for the cheapest price and end up with an inferior product. Where as people need to understand that a builder with the high price ( not astronomically higher 15-20% higher) are the ones with correct systems in place, a bide by correct OHS and use proper and correct product. If that can be conveyed through the website somehow, without saying it directly, it would be awesome.

Font styles to use
Sans Serif

Requirements
Must have
• I would like the testimonials to have a designated page (mentioned in the brief) but I would like the testimonials to be linked to the gallery page and when the picture are open of completed job the relevant testimonials would pop up near the pictures.

Nice to have
• I would like peolpe to understand that they are buy a price when they are getting quote to build there house. It seems like people just look for the cheapest price and end up with an inferior product. Where as people need to understand that a builder with the high price ( not astronomically higher 15-20% higher) are the ones with correct systems in place, a bide by correct OHS and use proper and correct product. If that can be conveyed through the website somehow, without saying it directly, it would be awesome.

```html
<!DOCTYPE html>
<html lang="en">
<head>
<meta charset="utf-8">
<title>Merrivale Construction</title>
<link rel="stylesheet" href="https://fonts.googleapis.com/css2?family=Cinzel:wght@700;900&family=Open+Sans:ital,wght@0,400;0,600;0,700;1,400&family=Poppins:wght@700&display=swap">
<style>
:root{
  --blue:#1474c4;
  --blue-dark:#0d5fa8;
  --ink:#222;
  --muted:#666;
  --pale:#e6f0f7;
  --light:#f3f3f3;
  --footer:#141414;
  --white:#fff;
}
*{box-sizing:border-box;margin:0;padding:0}
html,body{width:1200px;height:3161px;overflow:hidden}
body{position:relative;background:var(--white);font-family:"Open Sans",sans-serif;color:var(--ink)}
.abs{position:absolute}
.cinzel{font-family:"Cinzel",serif;font-weight:700}

/* top bar */
.topbar{top:0;left:0;width:1200px;height:34px;background:var(--blue);color:var(--white);font-size:13px}
.topbar .social{position:absolute;width:22px;height:22px;border:1.5px solid var(--white);border-radius:50%;top:6px}
.topbar .contact{position:absolute;top:9px;display:flex;align-items:center;gap:7px}
.topbar .divider{position:absolute;left:910px;top:9px;width:1px;height:16px;background:rgba(255,255,255,.5)}

/* nav */
.nav{top:34px;left:0;width:1200px;height:78px;background:var(--white);font-size:13px;color:#444}
.nav a{position:absolute;top:33px;color:inherit;text-decoration:none;transform:translateX(-50%)}
.nav a.active{color:var(--blue)}
.brand{position:absolute;display:flex;align-items:center;gap:8px;color:var(--blue);font-family:"Cinzel",serif;font-weight:700}
.brand .mark{border-radius:50%;background:var(--blue)}

/* hero */
.hero{top:112px;left:0;width:1200px;height:636px;background:linear-gradient(180deg,#5b8fc9 0%,#9bb6cf 35%,#b9b7ae 60%,#8f8a80 85%,#ffffff 100%)}
.hero-title{top:240px;width:1200px;text-align:center;font-family:"Poppins",sans-serif;font-size:49px;line-height:53px;color:var(--white);text-shadow:0 2px 6px rgba(0,0,0,.35)}
.hero-tag{top:360px;left:421px;width:358px;height:31px;background:var(--blue);color:var(--white);font-size:14px;text-align:center;line-height:31px}
.arrow{width:38px;height:38px;border-radius:50%}

/* features */
.feature{top:808px;width:245px;text-align:center}
.feature .icon{width:80px;height:80px;border-radius:50%;margin:0 auto;border:2px solid var(--blue);display:flex;align-items:center;justify-content:center}
.feature .icon.filled{background:var(--blue)}
.feature h3{font-family:"Cinzel",serif;font-size:19px;color:var(--blue);margin-top:22px;letter-spacing:1px}
.feature p{font-size:11.5px;line-height:21px;color:var(--muted);margin-top:9px}

/* about */
.about{top:1083px;left:0;width:1200px;height:450px;background:var(--pale);overflow:hidden}
.about h2{position:absolute;left:236px;top:68px;font-family:"Cinzel",serif;font-size:42px;color:var(--blue)}
.about h4{position:absolute;left:236px;top:122px;font-size:15px;font-weight:700}
.about .copy{position:absolute;left:239px;top:162px;width:330px;font-size:11.5px;line-height:21px;color:#555}
.about .copy p+p{margin-top:12px}
.pill{position:absolute;display:flex;align-items:center;justify-content:space-between;background:var(--blue);color:var(--white);border-radius:22px;font-family:"Cinzel",serif;font-weight:700;letter-spacing:1px}
.pill .dot{border-radius:50%;background:var(--white)}
.about-photo{position:absolute;left:663px;top:38px;width:368px;height:368px;border-radius:50%;background:radial-gradient(circle at 50% 60%,#c9d3e3 0%,#6f88bd 45%,#1b3fa6 100%)}

/* gallery */
.section-title{width:1200px;text-align:center;font-family:"Cinzel",serif;font-weight:700;color:var(--blue)}
.gallery-item{top:1709px;height:195px}
.round{width:38px;height:38px;border-radius:50%;border:1.5px solid}

/* testimonials */
.testimonials{top:2047px;left:0;width:1200px;height:337px;background:linear-gradient(180deg,#f6f6f6,#efefef)}
.avatar{left:323px;top:158px;width:92px;height:92px;border-radius:50%;border:3px solid var(--blue);background:radial-gradient(circle,#d9cfc6,#a99a8e)}
.quote{left:445px;top:168px;width:470px;font-style:italic;font-size:11.5px;line-height:22px;color:#555}
.client{left:445px;top:255px;font-family:"Cinzel",serif;font-weight:700;font-size:15px;letter-spacing:1px}

/* blog */
.blog{top:2384px;left:0;width:1200px;height:409px;background:linear-gradient(120deg,#1474c4,#1a6bb4 50%,#1474c4)}
.blog-photo{left:222px;top:151px;width:360px;height:183px;background:linear-gradient(180deg,#c9c2b8 0%,#8f8d86 55%,#4e7a3a 80%,#3d6a2c 100%)}
.blog-card{left:600px;top:151px;width:358px;height:183px;background:rgba(10,80,150,.55);color:var(--white);padding:24px 22px}
.blog-card h3{font-family:"Cinzel",serif;font-size:14.5px;line-height:22px;letter-spacing:.5px}
.blog-card p{font-size:11.5px;line-height:21px;margin-top:14px}
.blog-card .more{position:absolute;right:22px;bottom:26px;font-family:"Cinzel",serif;font-size:11px;font-style:italic;text-decoration:underline}

/* footer */
.footer{top:2793px;left:0;width:1200px;height:324px;background:linear-gradient(180deg,#1c1c1c,var(--footer));color:#bbb;font-size:11px}
.footer h5{position:absolute;font-family:"Cinzel",serif;font-size:15px;color:var(--blue);transform:translateX(-50%);white-space:nowrap;letter-spacing:.5px}
.footer .sitemap{position:absolute;left:478px;top:100px;transform:translateX(-50%);text-align:center;line-height:21px}
.field{position:absolute;left:611px;width:202px;background:var(--white);color:#888;font-size:10px;padding:8px 11px}
.fsocial{position:absolute;top:95px;width:30px;height:30px;border-radius:50%;background:var(--blue)}
.copyright{top:3117px;left:0;width:1200px;height:44px;background:var(--blue);color:var(--white);font-size:11px;text-align:center;line-height:44px}
</style>
</head>
<body>

<header class="abs topbar">
  <span class="social" style="left:162px"></span>
  <span class="social" style="left:189px"></span>
  <span class="social" style="left:218px"></span>
  <span class="social" style="left:245px"></span>
  <span class="contact" style="left:797px">
    <svg width="14" height="14" viewBox="0 0 24 24"><path fill="#fff" d="M6.6 10.8a15 15 0 0 0 6.6 6.6l2.2-2.2c.3-.3.7-.4 1-.2 1.1.4 2.3.6 3.6.6.6 0 1 .4 1 1V20c0 .6-.4 1-1 1A17 17 0 0 1 3 4c0-.6.4-1 1-1h3.5c.6 0 1 .4 1 1 0 1.3.2 2.5.6 3.6.1.3 0 .7-.2 1z"/></svg>
    <span style="font-size:14px">123 456 7890</span>
  </span>
  <span class="divider"></span>
  <span class="contact" style="left:925px">
    <svg width="14" height="11" viewBox="0 0 24 18"><path fill="#fff" d="M0 0h24v2L12 10 0 2zM0 4l12 8 12-8v14H0z"/></svg>
    <span>info@merrivale.com</span>
  </span>
</header>

<nav class="abs nav">
  <a href="#" class="active" style="left:331px">Home</a>
  <a href="#" style="left:400px">About Us</a>
  <a href="#" style="left:472px">Services</a>
  <div class="brand" style="left:527px;top:22px">
    <span class="mark" style="width:32px;height:32px"></span>
    <span style="font-size:20px">Merrivale</span>
  </div>
  <a href="#" style="left:724px">Gallery</a>
  <a href="#" style="left:800px">Testimonials</a>
  <a href="#" style="left:889px">Contact Us</a>
</nav>

<section class="abs hero" role="img" aria-label="Photo of a two-storey luxury home with stone facade and balcony under a blue sky">
  <h1 class="abs hero-title">High End Luxury<br>Custom Home Builder</h1>
  <div class="abs hero-tag">Merrivale CONSTRUCTION</div>
  <svg class="abs arrow" style="left:57px;top:279px" viewBox="0 0 38 38"><circle cx="19" cy="19" r="17.5" fill="none" stroke="#222" stroke-width="1.5"/><path d="M27 19H11m5-5-5 5 5 5" fill="none" stroke="#222" stroke-width="2"/></svg>
  <svg class="abs arrow" style="left:1101px;top:279px" viewBox="0 0 38 38"><circle cx="19" cy="19" r="19" fill="#1474c4"/><path d="M11 19h16m-5-5 5 5-5 5" fill="none" stroke="#fff" stroke-width="2"/></svg>
</section>

<section>
  <div class="abs feature" style="left:229px">
    <div class="icon filled"><svg width="40" height="40" viewBox="0 0 40 40" fill="none" stroke="#fff" stroke-width="1.8"><rect x="8" y="6" width="26" height="28"/><path d="M8 6 5 9v28l3-3M14 12h14v16H14zM21 12v8m-7 0h7m0 0v8"/></svg></div>
    <h3>Plan</h3>
    <p>Lorem Ipsum is simply dummy text of the printing and typesetting industry. Lorem Ipsum has been</p>
  </div>
  <div class="abs feature" style="left:478px">
    <div class="icon"><svg width="42" height="42" viewBox="0 0 42 42" fill="none" stroke="#1474c4" stroke-width="1.8"><rect x="7" y="8" width="26" height="24"/><path d="M12 20l8-7 8 7v8H12zM17 28v-5h6v5M33 10l4 2v22l-4-2M5 36h30"/></svg></div>
    <h3>Design</h3>
    <p>Lorem Ipsum is simply dummy text of the printing and typesetting industry. Lorem Ipsum has been</p>
  </div>
  <div class="abs feature" style="left:725px">
    <div class="icon"><svg width="44" height="44" viewBox="0 0 44 44" fill="none" stroke="#1474c4" stroke-width="1.8"><path d="M5 36h34M9 36V22l9-8 9 8v14M27 36V16h10v20M14 36v-8h8v8M30 22h4m-4 5h4M22 10h10l5 6"/></svg></div>
    <h3>Build</h3>
    <p>Lorem Ipsum is simply dummy text of the printing and typesetting industry. Lorem Ipsum has been</p>
  </div>
</section>

<section class="abs about">
  <svg class="abs" style="left:0;top:0" width="1200" height="450"><polygon points="1200,0 1200,450 751,450" fill="#1474c4"/></svg>
  <h2>Merrivale</h2>
  <h4>CONSTRUCTION</h4>
  <div class="copy">
    <p>Lorem Ipsum is simply dummy text of the printing and typesetting industry. Lorem Ipsum has been the industry's standard dummy text ever since the.</p>
    <p>Lorem Ipsum is simply dummy text of the printing and typesetting industry. Lorem Ipsum has been the industry's standard dummy text ever since the 1500s, when an unknown printer took a galley of type.</p>
  </div>
  <div class="pill" style="left:234px;top:334px;width:181px;height:41px;padding:0 5px 0 24px;font-size:14px">
    <span>Learn More</span><span class="dot" style="width:33px;height:33px"></span>
  </div>
  <div class="about-photo" role="img" aria-label="Photo of a modern white villa lit at dusk with a pool in front"></div>
</section>

<section>
  <h2 class="abs section-title" style="top:1600px;font-size:40px">Gallery</h2>
  <p class="abs" style="top:1655px;width:1200px;text-align:center;font-size:12px;font-weight:700">The Quality We Provide.</p>
  <div class="abs gallery-item" style="left:0;width:216px;background:linear-gradient(180deg,#4a6fa0,#3b4a5c 60%,#1f2630)" role="img" aria-label="Photo of a modern home and pool at dusk"></div>
  <div class="abs gallery-item" style="left:228px;width:252px;background:linear-gradient(180deg,#f2f2f2,#d8d6d2 60%,#6b4a32)" role="img" aria-label="Photo of a white curved staircase in a bright hallway"></div>
  <div class="abs gallery-item" style="left:491px;width:217px;background:linear-gradient(180deg,#6aa6e0,#b4773f 50%,#c9c3b6)" role="img" aria-label="Photo of a timber-clad modern house with garage"></div>
  <div class="abs gallery-item" style="left:719px;width:253px;background:linear-gradient(180deg,#eceae6,#c9c5bf 55%,#5a3a24)" role="img" aria-label="Photo of a white kitchen with dark timber floor"></div>
  <div class="abs gallery-item" style="left:983px;width:217px;background:linear-gradient(180deg,#e9eef2,#6f8a6e 45%,#9fd3df)" role="img" aria-label="Photo of an infinity pool overlooking a bay"></div>
  <svg class="abs round" style="left:558px;top:1929px;border:none" viewBox="0 0 38 38"><circle cx="19" cy="19" r="17.5" fill="none" stroke="#222" stroke-width="1.5"/><path d="M27 19H11m5-5-5 5 5 5" fill="none" stroke="#222" stroke-width="2"/></svg>
  <svg class="abs round" style="left:602px;top:1929px;border:none" viewBox="0 0 38 38"><circle cx="19" cy="19" r="17.5" fill="none" stroke="#1474c4" stroke-width="1.5"/><path d="M11 19h16m-5-5 5 5-5 5" fill="none" stroke="#1474c4" stroke-width="2"/></svg>
</section>

<section class="abs testimonials">
  <h2 class="abs section-title" style="top:70px;font-size:40px;left:-15px">Testimonials</h2>
  <svg class="abs" style="left:258px;top:190px" width="14" height="28" viewBox="0 0 14 28"><path d="M12 2 2 14l10 12" fill="none" stroke="#999" stroke-width="1.5"/></svg>
  <svg class="abs" style="left:962px;top:190px" width="14" height="28" viewBox="0 0 14 28"><path d="M2 2l10 12L2 26" fill="none" stroke="#999" stroke-width="1.5"/></svg>
  <div class="abs avatar" role="img" aria-label="Portrait of the client"></div>
  <p class="abs quote">" Lorem Ipsum is simply dummy text of the printing and typesetting The industry. Lorem Ipsum has been the industry's standard dummy text ever since the 1500s, when an unknown industry's standard dummy text&nbsp; "</p>
  <p class="abs client">— Client Name</p>
</section>

<section class="abs blog">
  <h2 class="abs section-title" style="top:66px;font-size:40px;color:#fff">Blog Post</h2>
  <div class="abs blog-photo" role="img" aria-label="Rendering of a two-storey contemporary home with lawn"></div>
  <article class="abs blog-card">
    <h3>Lorem Ipsum is simply dummy text of the printing &amp; type.</h3>
    <p>Lorem Ipsum is simply dummy text of the printing and type setting industry. Lorem Ipsum has been the Thisis standard dummy text ever since the 1500s.</p>
    <span class="more">Read More ▸</span>
  </article>
</section>

<footer class="abs footer">
  <div class="brand" style="left:161px;top:34px">
    <span class="mark" style="width:40px;height:40px"></span>
    <span style="font-size:24px">Merrivale</span>
  </div>
  <svg class="abs" style="left:162px;top:113px" width="14" height="20" viewBox="0 0 14 20"><path fill="#1474c4" d="M7 0a7 7 0 0 0-7 7c0 5 7 13 7 13s7-8 7-13a7 7 0 0 0-7-7zm0 10a3 3 0 1 1 0-6 3 3 0 0 1 0 6z"/></svg>
  <p class="abs" style="left:190px;top:110px;line-height:20px">Merrivale Construction<br>101 - Lorem ipsum simple<br>simple text print.</p>
  <svg class="abs" style="left:162px;top:188px" width="14" height="14" viewBox="0 0 24 24"><path fill="#1474c4" d="M6.6 10.8a15 15 0 0 0 6.6 6.6l2.2-2.2c.3-.3.7-.4 1-.2 1.1.4 2.3.6 3.6.6.6 0 1 .4 1 1V20c0 .6-.4 1-1 1A17 17 0 0 1 3 4c0-.6.4-1 1-1h3.5c.6 0 1 .4 1 1 0 1.3.2 2.5.6 3.6.1.3 0 .7-.2 1z"/></svg>
  <p class="abs" style="left:190px;top:186px;font-size:13px;font-weight:600;color:var(--blue)">123 456 7890</p>
  <svg class="abs" style="left:162px;top:221px" width="14" height="11" viewBox="0 0 24 18"><path fill="#1474c4" d="M0 0h24v2L12 10 0 2zM0 4l12 8 12-8v14H0z"/></svg>
  <p class="abs" style="left:190px;top:219px">info@merrivale.com</p>

  <h5 style="left:478px;top:50px">Sitemap</h5>
  <div class="sitemap">Home<br>About Us<br>Services<br>Gallery<br>Testimonial<br>Contact Us</div>

  <h5 style="left:706px;top:50px">Contact Us</h5>
  <div class="field" style="top:95px;height:29px">Name *</div>
  <div class="field" style="top:131px;height:27px">Email *</div>
  <div class="field" style="top:165px;height:50px">Message *</div>
  <div class="pill" style="left:642px;top:226px;width:133px;height:39px;padding:0 4px 0 22px;font-size:14px">
    <span>Submit</span><span class="dot" style="width:31px;height:31px"></span>
  </div>

  <h5 style="left:937px;top:50px">Follow Us</h5>
  <span class="fsocial" style="left:867px"></span>
  <span class="fsocial" style="left:904px"></span>
  <span class="fsocial" style="left:942px"></span>
  <span class="fsocial" style="left:980px"></span>
</footer>

<div class="abs copyright">©Merrivale Construction - 2020 All rights reserved</div>

</body>
</html>
```